New Jar Label for Manuka Honey Company!

Hine Roa Honey, a Manuka Honey company from New Zealand is looking for a fresh & engaging label for our manuka honey jars.

Attached are some examples of label designs that we like, feel free to use the language/copy on these labels for inspiration/content/copy, but feel free to add your own creative spin if you have a great design idea!

LABEL DIMENSIONS: 1654mmx532mm

Label Must Include:
- MGO rating
- Made (or) Product of New Zealand
- Manuka Honey (can add extra text similar to attached examples)

Label Can Include:
- Badges: raw food, non gmo, bpa free, gluten free, halal etc
- anything you feel is appropriate

You can change the color of the logo(s) to Black, White, Silver or Gold.

Can you please include a mockup of your label design(s) on the supplied "Jar Mockup File". You can change the scene of the mockup if you like.

UPDATE:

Have decided on bee logo so please bo longer use the mountain logo for label mockups. Design(s) will need multiple color variations to represent the other MGO ratings, flavor combos and other honey types, other than manuka.

• Provide multiple designs for each honey type
Manuka Design
Spring Honey Design
MGO 100-1000 Design(s)
Wildflower Honey Design
Flavor Combo Honey Design

```html
<!DOCTYPE html>
<html lang="en">
<head>
<meta charset="utf-8">
<title>Hine Roa Honey – Manuka Honey Jar Label</title>
<link rel="stylesheet" href="https://fonts.googleapis.com/css2?family=Montserrat:wght@300;400;500;600;700&family=Roboto:wght@400;500;700&display=swap">
<style>
  :root{
    --page:#eceeea;
    --label-white:#ffffff;
    --band-dark:#2e2325;
    --band-dark-2:#3a2d30;
    --gold-light:#f7dc82;
    --gold-mid:#d7aa45;
    --gold-deep:#a8782a;
    --ink:#2f2527;
    --ink-soft:#c9c0c0;
    --text-light:#e9e4e4;
  }
  *{box-sizing:border-box;margin:0;padding:0}
  html,body{width:1200px;height:857px;overflow:hidden;background:var(--page)}
  body{font-family:"Montserrat",sans-serif;position:relative}

  .label{position:absolute;left:40px;top:112px;width:1120px;height:632px;background:var(--label-white);box-shadow:0 6px 24px rgba(0,0,0,.12)}
  .gold-band{position:absolute;left:0;width:100%;background:linear-gradient(90deg,var(--gold-deep),var(--gold-light) 30%,var(--gold-mid) 55%,var(--gold-light) 80%,var(--gold-deep))}
  .gold-band--top{top:7px;height:22px}
  .gold-band--rule{top:402px;height:8px}

  .pattern-band{position:absolute;left:0;top:29px;width:100%;height:367px;background:radial-gradient(ellipse at 50% 40%,var(--band-dark-2),var(--band-dark) 70%)}

  .ingredients{position:absolute;left:37px;top:120px;width:216px;color:var(--text-light)}
  .ingredients h3{font-size:11.5px;font-weight:600;letter-spacing:.2px;margin-bottom:9px}
  .ingredients p{font-size:9.6px;line-height:13.7px;text-align:justify;margin-bottom:16px;font-weight:400}

  .brand-name{position:absolute;left:0;width:100%;top:112px;text-align:center;font-size:24px;font-weight:700;color:var(--gold-mid);letter-spacing:.3px}
  .brand-mark{display:block;width:14px;height:14px;margin:0 auto 10px;border-radius:50%;background:var(--gold-mid)}

  .gold-text{background:linear-gradient(180deg,var(--gold-light),var(--gold-mid) 55%,var(--gold-deep));-webkit-background-clip:text;background-clip:text;color:transparent}
  .product-title{position:absolute;left:0;width:100%;top:196px;text-align:center;font-size:76px;font-weight:600;line-height:80px;letter-spacing:1px}
  .product-sub{position:absolute;left:0;width:100%;top:354px;text-align:center;font-size:19px;font-weight:300;color:var(--ink-soft);letter-spacing:.5px}

  .nutrition{position:absolute;left:868px;top:119px;width:202px;height:255px;background:var(--label-white);border:1px solid #fff;outline:1px solid var(--ink);outline-offset:-4px;padding:6px 8px;font-family:"Roboto",sans-serif;color:#000}
  .nutrition h4{font-size:23px;font-weight:500;line-height:26px;border-bottom:1px solid #000;margin-bottom:2px}
  .nutrition .row{display:flex;justify-content:space-between;font-size:8.5px;line-height:13px;border-bottom:1px solid #000}
  .nutrition .row.plain{border-bottom:none}
  .nutrition .thick{border-bottom:6px solid #000}
  .nutrition .serv{font-size:10.5px;font-weight:700}
  .nutrition .big{font-size:19px;font-weight:500;line-height:22px;border-bottom:4px solid #000}
  .nutrition .right{justify-content:flex-end;font-weight:700}
  .nutrition .indent{padding-left:11px}
  .nutrition b{font-weight:700}

  .badges{position:absolute;left:37px;top:456px;display:flex;gap:16px;align-items:flex-start}
  .badge-square{width:64px;height:64px;background:var(--ink)}
  .badge-circle{width:64px;height:64px;border-radius:50%;background:#111}
  .badge-recycle{width:58px;height:64px}

  .batch-info{position:absolute;left:37px;top:548px;font-size:27px;line-height:35px;color:#111;font-family:"Roboto",sans-serif}

  .mgo{position:absolute;left:0;width:100%;top:426px;text-align:center;font-size:72px;font-weight:700;line-height:70px;color:var(--ink)}
  .origin{position:absolute;left:0;width:100%;top:566px;text-align:center;font-size:17px;font-weight:600;color:var(--ink)}
  .net-weight{position:absolute;left:450px;top:598px;width:220px;height:30px;background:linear-gradient(90deg,transparent,var(--gold-light) 12%,var(--gold-mid) 50%,var(--gold-light) 88%,transparent);display:flex;align-items:center;justify-content:center;font-size:15px;color:var(--ink);font-weight:500}
</style>
</head>
<body>
  <section class="label" aria-label="Manuka honey jar label, flat">
    <div class="gold-band gold-band--top"></div>
    <div class="pattern-band" role="img" aria-label="Dark carved-style decorative pattern background"></div>
    <div class="gold-band gold-band--rule"></div>

    <div class="ingredients">
      <h3>INGREDIENTS</h3>
      <p>Lorem ipsum dolor sit amet, consectetuer adipiscing elit, sed diam nonummy nibh euismod tincidunt ut laoreet dolore magna aliquam erat volutpat. Ut wisi enim ad minim veniam, quis nostrud exerci tation ullamcorper suscipit lobortis nisl ut aliquip ex ea commodo</p>
      <h3>INGREDIENTS</h3>
      <p>Lorem ipsum dolor sit amet, consectetuer adipiscing elit, sed diam nonummy nibh euismod tincidunt ut laoreet dolore magna aliquam erat volutpat. Ut wisi enim ad minim veniam, quis nostrud exerci tation ullamcorper suscipit lobortis nisl ut aliquip ex ea commodo</p>
    </div>

    <div class="brand-name"><span class="brand-mark"></span>Hine Roa Honey</div>
    <h1 class="product-title gold-text">MANUKA<br>HONEY</h1>
    <p class="product-sub">CERTIFIED MGO CONTENT</p>

    <div class="nutrition">
      <h4>Nutrition Facts</h4>
      <div class="row plain" style="font-size:10px">12 servings per container</div>
      <div class="row thick serv"><span>Serving size</span><span>1 Tbsp (15g)</span></div>
      <div class="row plain" style="font-size:7.5px;font-weight:700;line-height:11px">Amount per serving</div>
      <div class="row big"><span>Protien</span><span>14</span></div>
      <div class="row right"><span>% Daily Value*</span></div>
      <div class="row"><span><b>Total Fat</b> 1.5g</span><b>2%</b></div>
      <div class="row indent"><span>Saturated Fat 0g</span><b>0%</b></div>
      <div class="row indent"><span>Trans Fat 0g</span><span></span></div>
      <div class="row"><span><b>Cholesterol</b> 0mg</span><b>0%</b></div>
      <div class="row"><span><b>Sodium</b> 70mg</span><b>3%</b></div>
      <div class="row"><span><b>Total Carbohydrate</b> 2g</span><b>1%</b></div>
      <div class="row indent"><span>Dietary Fiber 0g</span><b>0%</b></div>
      <div class="row indent plain"><span>Total Sugars 1g</span><span></span></div>
    </div>

    <div class="badges">
      <div class="badge-square" role="img" aria-label="Certification badge"></div>
      <div class="badge-circle" role="img" aria-label="BPA free badge"></div>
      <svg class="badge-recycle" viewBox="0 0 58 64" role="img" aria-label="Recycling mark">
        <path d="M29 6 L52 46 L6 46 Z" fill="none" stroke="#111" stroke-width="3" stroke-linejoin="round"/>
      </svg>
    </div>

    <div class="batch-info">BB:<br>Batch:</div>

    <div class="mgo">MGO<br>100+</div>
    <p class="origin">PRODUCT OF NEWZEALAND</p>
    <div class="net-weight">℮ 250g (8.8oz) NET Wt.</div>
  </section>
</body>
</html>
```